vexlo-compatible banner ad set and associated landing page design

This is the message that the banner should communicate:
"Get Paid to Save the Planet - Solar Pays You Up to $750+ Every Year for Use of Your Roof"
BANNER SIZE:  300x250 would be great. (After choosing the winner, we will pay additional money to create new versions indifferent sizes as a follow-on work.)
BANNER FORMAT:  Could be an animated GIF, static JPG HTML 5, video, your call.
As for design guidelines for the ad and landing page, follow design guidance at: http://qe-tx47.leadvorn.com/rs/pivotrally/images/10%20blunders%20layout_final%20(1).pdf
The banner ad will be used on the Vexlo Ad network and should have a call to action to get the user to click to the landing page. The call to action can be two buttons within the banner ad:
"I Care About Planet Earth"
"Don't Care"
Clicking anywhere on the banner ad will drive traffic to the landing page.
On the landing page, we want a design that we can implement in pagemorrel.com to capture the following information:
- Street Number and Street Name of My Home
- My Zip Code
- Name of My Electric Utility
- My Typical Monthly Electric Bill Amount is:
- How Much I'd Like to Earn From Solar Per-Year?
After the user fills out the above, the following questions drop down:
First Name
Last Name
Email Address
Phone Number
At the end of the data entry portion of the landing page, there should be a "call to action" button.
LANDING PAGE FORMAT:  Photoshop or jpg format or html5 format would be great.

Updates
Target Market(s)
home owners
Industry/Entity Type
Home Improvement
Requirements
Nice to have
- Follow design guidance at: http://qe-tx47.leadvorn.com/rs/pivotrally/images/10%20blunders%20layout_final%20(1).pdf

```html
<!DOCTYPE html>
<html lang="en">
<head>
<meta charset="UTF-8">
<title>Do You Care About Planet Earth? — Banner</title>
<link rel="stylesheet" href="https://fonts.googleapis.com/css2?family=Montserrat:wght@500;600&display=swap">
<style>
  :root {
    --stage-bg: #0b0b0b;
    --banner-green: #7aa117;
    --banner-green-deep: #6f9414;
    --banner-edge: #ffffff;
    --headline: #ffffff;
    --care-fill: #fde424;
    --care-edge: #fff27a;
    --care-text: #1e1e1e;
    --decline-fill: #be2e0b;
    --decline-edge: #a9c22c;
    --decline-text: #ffffff;
  }
  * { box-sizing: border-box; margin: 0; padding: 0; }
  html, body {
    width: 1200px;
    height: 900px;
    overflow: hidden;
    background: var(--stage-bg);
  }
  .stage {
    position: relative;
    width: 1200px;
    height: 900px;
  }
  .banner {
    position: absolute;
    left: 374px;
    top: 261px;
    width: 452px;
    height: 377px;
    border: 1.5px solid var(--banner-edge);
    background: var(--banner-green);
    overflow: hidden;
    font-family: "Montserrat", sans-serif;
  }
  .banner__pattern {
    position: absolute;
    inset: 0;
    background: radial-gradient(ellipse at 50% 45%, var(--banner-green) 0%, var(--banner-green-deep) 100%);
  }
  .banner__headline {
    position: absolute;
    left: 0;
    right: 0;
    top: 50px;
    text-align: center;
    color: var(--headline);
    font-weight: 600;
    font-size: 35px;
    line-height: 48px;
    letter-spacing: -0.2px;
  }
  .banner__button {
    position: absolute;
    left: 82px;
    width: 286px;
    height: 71px;
    border-radius: 8px;
    display: flex;
    align-items: center;
    justify-content: center;
    font-weight: 500;
    text-decoration: none;
  }
  .banner__button--care {
    top: 184px;
    background: var(--care-fill);
    border: 2.5px solid var(--care-edge);
    color: var(--care-text);
    font-size: 34px;
  }
  .banner__button--decline {
    top: 275px;
    background: var(--decline-fill);
    border: 2.5px solid var(--decline-edge);
    color: var(--decline-text);
    font-size: 30px;
  }
</style>
</head>
<body>
  <main class="stage">
    <a class="banner" href="#landing" aria-label="Do You Care About Planet Earth? banner">
      <div class="banner__pattern" role="img" aria-label="Faint pattern of eco icons: bicycles, recycling bins, leaves, flames, clouds and solar panels"></div>
      <h1 class="banner__headline">Do You Care<br>About Planet Earth?</h1>
      <span class="banner__button banner__button--care">I Care</span>
      <span class="banner__button banner__button--decline">I Don’t Care</span>
    </a>
  </main>
</body>
</html>
```